Nobody Left the Lantern Burning - Tom Halvery - CD Cover Design Project

Single Cover for CD & Online media e.g. Tunebox Graphics
The first song release from Tom Halvery will be the track 'Nobody Left the Lantern Burning'.
For the release the single requires artwork that is eye catching, seriously professional & meets the requirements of Disc Sprout, Tunebox and also a physical copy on CD.
Track listings for CD will be:
1. Nobody Left the Lantern Burning
2. Nobody Left the Lantern Burning - Instrumental
see details in this link:
http://members.discsprout-example.com/faq.aspx
http://selfmadesound.discsprout-example.com/2009/11/avoid-album-art-atrocities/
http://answers.quorvex-example.com/question/index?qid=20111015141433AAdDTmH
Any advice on this would be greatly appreciated,
I would also like the two logo's I have uploaded to be used,
one is the Tom Halvery logo and the other is for Milbrook & Tandy Records logo (please remove the R and replace with a C for copyright.)
There are four high res photo shopped pictures of Tom Halvery and another zip file of many others, it would be nice to include one of these maybe on the 2nd page or back of the CD. Please don't use them as the front cover.
I imagine an Art Deco illustration but please listen to the track and let it inspire you.
Good Luck
Updates
I don't feel this is what I'm looking for, the design needs to refelct a broken heart without being a picture of a broken heart
Reason: No design has been what we are after so far so the deadline has been extended and the budget increased.

```html
<!DOCTYPE html>
<html lang="en">
<head>
<meta charset="utf-8">
<title>Nobody Left the Lantern Burning – Tom Halvery – CD Insert</title>
<link rel="stylesheet" href="https://fonts.googleapis.com/css2?family=Parisienne&family=Raleway:wght@300;500&display=swap">
<style>
  :root {
    --stage: #e9e7e6;
    --paper: #f3e3dc;
    --paper-deep: #e8cfc6;
    --rose: #c99ea1;
    --band: rgba(201, 150, 155, 0.75);
    --band-light: rgba(214, 160, 164, 0.55);
    --script-faint: rgba(190, 140, 140, 0.3);
    --white: #ffffff;
    --label-ink: #4a2a30;
    --petal: #f2aeb3;
    --petal-soft: #f6c7c8;
    --letter-paper: #e9c3b9;
  }
  * { margin: 0; padding: 0; box-sizing: border-box; }
  html, body { width: 1200px; height: 1015px; overflow: hidden; }
  body { background: var(--stage); position: relative; }

  .insert {
    position: absolute;
    left: 40px; top: 232px;
    width: 1120px; height: 550px;
    box-shadow: 0 6px 18px rgba(0,0,0,0.18);
  }

  /* Back panel */
  .back-panel {
    position: absolute; left: 0; top: 0;
    width: 547px; height: 550px;
    background: linear-gradient(135deg, var(--paper) 0%, #f6e9e2 50%, var(--paper-deep) 100%);
    overflow: hidden;
  }
  .title-echoes {
    position: absolute; left: 0; top: 0;
    width: 547px; height: 290px;
  }
  .title-echo {
    position: absolute;
    font-family: "Parisienne", cursive;
    font-size: 24px;
    line-height: 1;
    color: var(--script-faint);
    white-space: nowrap;
    transform: rotate(-10deg);
    transform-origin: left center;
  }
  .artist-photo {
    position: absolute; left: 163px; top: 0;
    width: 384px; height: 550px;
    background: linear-gradient(160deg, rgba(120,90,80,0.3) 0%, rgba(230,205,195,0.45) 45%, rgba(90,70,65,0.55) 100%);
  }
  .tracklist-band {
    position: absolute; left: 0; top: 296px;
    width: 512px; height: 139px;
    background: var(--band);
    padding: 16px 0 0 40px;
    color: var(--white);
    font-family: "Parisienne", cursive;
  }
  .tracklist-band h2 { font-weight: 400; font-size: 24px; margin-bottom: 16px; }
  .tracklist-band ol { list-style: none; font-size: 21px; line-height: 1.6; }

  .label-marks {
    position: absolute; left: 26px; top: 470px;
    display: flex; gap: 22px; align-items: center;
    font-family: "Raleway", sans-serif; font-weight: 500;
    font-size: 12px; color: var(--label-ink);
  }
  .label-mark { display: flex; align-items: center; gap: 6px; }
  .label-mark .dot { width: 14px; height: 14px; background: var(--label-ink); border-radius: 50%; }
  .label-mark .square { width: 14px; height: 14px; background: var(--label-ink); }

  /* Spine */
  .spine {
    position: absolute; left: 547px; top: 0;
    width: 29px; height: 550px;
    background: var(--rose);
    display: flex; align-items: center; justify-content: center;
  }
  .spine-text {
    transform: rotate(90deg);
    white-space: nowrap;
    color: var(--white);
    display: flex; gap: 22px; align-items: baseline;
  }
  .spine-text .spine-title { font-family: "Parisienne", cursive; font-size: 18px; }
  .spine-text .spine-artist { font-family: "Raleway", sans-serif; font-weight: 300; font-size: 14px; letter-spacing: 1px; }

  /* Front panel */
  .front-panel {
    position: absolute; left: 576px; top: 0;
    width: 544px; height: 550px;
    overflow: hidden;
    background: linear-gradient(135deg, #dfa9a3 0%, #ecc1ba 45%, #d69f9c 100%);
  }
  .letters-photo {
    position: absolute; left: 250px; top: 0;
    width: 294px; height: 330px;
    background: linear-gradient(200deg, #f1d2c9 0%, var(--letter-paper) 55%, rgba(233,195,185,0) 100%);
  }
  .flower-photo {
    position: absolute; left: 80px; top: 120px;
    width: 300px; height: 300px;
    border-radius: 50%;
    background: radial-gradient(circle at 50% 48%, var(--petal-soft) 0%, var(--petal) 38%, rgba(240,170,175,0.6) 60%, rgba(230,170,170,0) 72%);
  }
  .title-band {
    position: absolute; left: 16px; top: 43px;
    width: 474px; height: 53px;
    background: var(--band-light);
    display: flex; align-items: center; justify-content: center;
    font-family: "Parisienne", cursive;
    font-size: 30px; color: var(--white);
  }
  .artist-name {
    position: absolute; left: 0; right: 0; top: 448px;
    text-align: center;
    font-family: "Raleway", sans-serif; font-weight: 300;
    font-size: 50px; color: var(--white);
    letter-spacing: 1px;
  }
</style>
</head>
<body>
  <div class="insert">
    <section class="back-panel">
      <div class="title-echoes" aria-hidden="true">
        <span class="title-echo" style="left:250px;top:70px">Nobody Left the Lantern</span>
        <span class="title-echo" style="left:60px;top:120px">Nobody Left the Lantern</span>
        <span class="title-echo" style="left:20px;top:180px">the Lantern Burning</span>
        <span class="title-echo" style="left:250px;top:170px">Nobody Left</span>
        <span class="title-echo" style="left:-10px;top:240px">Burning</span>
        <span class="title-echo" style="left:140px;top:255px">Nobody Left the Lantern</span>
      </div>
      <div class="artist-photo" role="img" aria-label="Photo of the artist reading from a notebook"></div>
      <div class="tracklist-band">
        <h2>Tracklisting:</h2>
        <ol>
          <li>1. Nobody Left the Lantern Burning</li>
          <li>2. Nobody Left the Lantern Burning - Instrumental</li>
        </ol>
      </div>
      <div class="label-marks">
        <div class="label-mark"><span class="dot"></span>Milbrook &amp; Tandy Records</div>
        <div class="label-mark"><span class="square"></span>Tom Halvery</div>
      </div>
    </section>

    <section class="spine">
      <div class="spine-text">
        <span class="spine-title">Nobody Left the Lantern Burning</span>
        <span class="spine-artist">TOM HALVERY</span>
      </div>
    </section>

    <section class="front-panel">
      <div class="letters-photo" role="img" aria-label="Old handwritten letters on aged paper"></div>
      <div class="flower-photo" role="img" aria-label="Soft pink carnation resting on the letters"></div>
      <div class="title-band">Nobody Left the Lantern Burning</div>
      <div class="artist-name">TOM HALVERY</div>
    </section>
  </div>
</body>
</html>
```